Mobile phone accessories

Hi all,
We're a distributor for mobile phone accessories.
We are looking for some creative designers to help us come up with re-designed packaging for all our mobile phone accessories.
For products like car chargers, travel chargers, and different kind of cases we currently use a plastic blister.
In this plastic blister we use an inner carton with the specific product lines (cover, TPU case, car charger etc).
We want to re-design this inner carton. Not only the color but also design (see examples in the file: example_blister_plastic.jpg).
At the moment we prefer numbers 2 and 3 because you can see the products better in this packing. We're open to other designs!
We want to use an anthracite color for the overall color (like pantone 19-3907 TPX)
And for the different packing lines, for example, these colors to "high light" the packing:
Screen protectors: Bright Blue
Chargers: Bright Orange
Covers: Bright Red
Car holders: Bright Green
Screenprotector:
We have 5 different kinds of screenprotectors. Each kind has to have it's own design but the basic design and color should be the same.
5 designs: Clear, Matt, Anti Scratch, Mirror, Privacy
In the attachment is our current design travenor_screenprotector) and also an example what we like (screenprotector_sample).
At the front we use stickers for the correct model, for example: for Vextor Zondra 4
We will still be using this sticker but above the sticker we want this text: Perfect fit for:
We want to place this sticker at the lower right or left corner.
At the back we want to add what the package contains:
2 screen protectors
1 x Microfiber cloth
1 x Scraper
The rest you can fill in yourself and also use the text in our current design.
At the front you have to remove the word: anti scratch
Slide case:
We have another brand (called Qurlo) for our higher-end slide cases. In the attachment is the die cut for this design that you can use for the size.
You can also use the text on the backside for our brand Travenor but we want a total different design for the total packing.
Logo:
We also updated our (new) logo which you can use (see attached file travenor_logo). We dont have a specific color for our logo.
Any questions, please dont hasitate to contact us!
The design needs to be minimal, modern, but still friendly.
The quality of our accessories are mid- to high level. Our design needs to exposure this look-and-feel.

```html
<!DOCTYPE html>
<html lang="en">
<head>
<meta charset="utf-8">
<title>Travenor Slide Case – Dieline</title>
<link rel="stylesheet" href="https://fonts.googleapis.com/css2?family=Arimo&family=Montserrat:wght@800&display=swap">
<style>
  :root {
    --paper: #ffffff;
    --pack-red: #e8412b;
    --window-white: #ffffff;
    --fold-line: #7a3a30;
    --ink: #111111;
    --label-ink: #1a1a1a;
    --device-light: #e9e4da;
    --device-dark: #9a9488;
  }
  * { margin: 0; padding: 0; box-sizing: border-box; }
  html, body {
    width: 800px;
    height: 1200px;
    overflow: hidden;
    background: var(--paper);
  }
  .dieline {
    position: relative;
    width: 800px;
    height: 1200px;
  }
  .dieline__art {
    position: absolute;
    inset: 0;
    width: 800px;
    height: 1200px;
  }
  .panel-label {
    position: absolute;
    font-family: "Arimo", Arial, sans-serif;
    color: var(--label-ink);
    font-weight: 400;
    line-height: 1;
  }
  .panel-label--front { left: 72px; top: 312px; font-size: 44px; }
  .panel-label--back  { left: 100px; top: 818px; font-size: 56px; }
  .brand-name {
    position: absolute;
    left: 285px;
    width: 494px;
    top: 805px;
    text-align: center;
    font-family: "Montserrat", Arial, sans-serif;
    font-weight: 800;
    font-size: 64px;
    letter-spacing: 1px;
    color: var(--ink);
  }
</style>
</head>
<body>
<main class="dieline">
  <svg class="dieline__art" viewBox="0 0 300 450" preserveAspectRatio="none" aria-hidden="false">
    <defs>
      <linearGradient id="device-fill" x1="0" y1="0" x2="1" y2="1">
        <stop offset="0" stop-color="var(--device-light)"/>
        <stop offset="1" stop-color="var(--device-dark)"/>
      </linearGradient>
    </defs>

    <!-- tuck tabs -->
    <path class="tab tab--top" d="M148 42 A52 40 0 0 1 252 42 Z" fill="var(--pack-red)"/>
    <path class="tab tab--bottom" d="M148 406 A52 36 0 0 0 252 406 Z" fill="var(--pack-red)"/>

    <!-- main board -->
    <rect class="board" x="107" y="40" width="185" height="370" fill="var(--pack-red)"/>

    <!-- front display window -->
    <ellipse class="window" cx="200" cy="108" rx="75" ry="62" fill="var(--window-white)"/>

    <!-- product in window -->
    <g class="product-shot" role="img" aria-label="Product photo: Zondra 4 smartphone showing its home screen, held inside the slide case">
      <rect x="162" y="64" width="78" height="100" rx="8" fill="url(#device-fill)"/>
      <rect x="167" y="76" width="68" height="72" fill="#c9b48a" opacity="0.55"/>
    </g>

    <!-- holding insert with V notch -->
    <polygon class="insert" points="140,124 200,160 260,124 260,176 140,176" fill="var(--pack-red)"/>

    <!-- fold lines -->
    <g class="folds" stroke="var(--fold-line)" stroke-width="0.5" stroke-dasharray="1.2 1.2" fill="none">
      <line x1="148" y1="42" x2="148" y2="406"/>
      <line x1="252" y1="42" x2="252" y2="406"/>
      <line x1="107" y1="52" x2="292" y2="52"/>
      <line x1="107" y1="175" x2="292" y2="175"/>
      <line x1="107" y1="210" x2="292" y2="210"/>
      <line x1="107" y1="400" x2="292" y2="400"/>
    </g>
  </svg>

  <p class="panel-label panel-label--front">Front</p>
  <p class="panel-label panel-label--back">Back</p>
  <p class="brand-name">Travenor</p>
</main>
</body>
</html>
```